Electronic Refurbishment Warehouse needs a Website

We are looking for a clean, professional looking design with iconic imagery. Our main point we want to get across is that we will help clients save time, and money, and provide outstanding quality. Our logo can be found in the uploads section. This site is used to impress clients that we have a pre-existing relationship with. This site will be available for the public but it will not be used to advertise to the public or to drive traffic to it. The color scheme we are looking to stay with is blue, but that is not to say that everything should be a shade of blue. Last note, see site map below.

Site Map:

Home
Company
a. company overview
b. CEO letter
Services
a. Remanufacture & Refurbishment Services
1. Consumer Electronics
2. Cellular Phones
b.Reverse Logistics Management
c.Warranty Repair & Field Services
d.Quality Control & Assurance
e.Warehousing & Distribution
Careers
Contact Us

Reason: We want to allocate more time for designers to do what they do best.

Target Market(s)

Phone and TV Retailers that may have units that need to be refurbished. Example Velorin, tallcart, qvo, etc.

Industry/Entity Type

Electronics

Requirements
Must have
• Home Page Slider.
Iconic imagery and navigation.
The ability to be put into the 960 Grid.

```html
<!DOCTYPE html>
<html lang="en">
<head>
<meta charset="utf-8">
<title>Brinmoor Group – Services</title>
<link rel="stylesheet" href="https://fonts.googleapis.com/css2?family=Roboto:wght@300;400&family=Open+Sans:wght@400;600;700&family=Arimo:wght@400;700&display=swap">
<style>
:root{
  --nav-blue:#1b5f8c;
  --nav-active:#5aa6cf;
  --link-blue:#1a72b4;
  --hero-top:#3f9ccb;
  --hero-bottom:#6fc2e6;
  --text-dark:#3a3a3a;
  --text-body:#666;
  --panel:#efefef;
  --footer-top:#7ea9c9;
  --footer-bottom:#5b95c5;
  --green-top:#9fdc4a;
  --green-bottom:#5fae1e;
}
*{margin:0;padding:0;box-sizing:border-box}
html,body{width:873px;height:1200px;overflow:hidden}
body{position:relative;background:var(--panel);font-family:'Arimo',sans-serif}
.abs{position:absolute}

.site-header{left:0;top:0;width:873px;height:86px;background:linear-gradient(#e9e9e9,#dedede);border-bottom:2px solid #c9c9c9}
.brand{left:29px;top:37px;display:flex;align-items:center;gap:8px}
.brand-mark{width:36px;height:36px;background:#4a8fc4}
.brand-name{font-family:'Roboto',sans-serif;font-size:13px;color:#4a8fc4;letter-spacing:.5px;border-left:2px solid #4a8fc4;padding-left:6px}
.main-nav a{position:absolute;top:54px;font-family:'Roboto',sans-serif;font-size:15.5px;color:var(--nav-blue);text-decoration:none}
.main-nav a.active{color:var(--nav-active)}
.sub-band{left:0;top:86px;width:873px;height:19px;background:linear-gradient(#fafafa,#e5e5e5)}
.pointer{left:579px;top:78px}

.hero{left:0;top:105px;width:873px;height:259px;background:radial-gradient(ellipse at 70% 110%,var(--hero-bottom),var(--hero-top) 75%);border-top:2px solid #2f86b5;border-bottom:2px solid #2f86b5}
.hero-image{left:68px;top:9px;width:223px;height:236px;background:linear-gradient(#c9a676,#a9855a);border-radius:3px}
.hero-title{left:312px;top:30px;font-family:'Roboto',sans-serif;font-weight:300;font-size:26px;line-height:28px;color:#fff}
.cta{left:615px;top:182px}

.services{left:0;top:364px;width:873px;height:163px;background:#fff;border-bottom:3px solid #d4d4d4}
.service{position:absolute;top:22px;width:170px;text-align:center}
.service-icon{width:96px;height:68px;margin:0 auto 10px;border-radius:4px}
.service-label{font-family:'Open Sans',sans-serif;font-size:13px;line-height:16px;color:var(--link-blue)}
.divider{position:absolute;top:38px;width:1px;height:62px;background:#d8d8d8}

.section-title{font-family:'Open Sans',sans-serif;font-weight:700;font-size:16px;line-height:17px;color:var(--text-dark);letter-spacing:.3px}
.about{left:28px;top:553px;width:340px}
.about p{font-size:11px;line-height:16.4px;color:var(--text-body);margin-top:17px}
.about p + p{margin-top:12px}
.photo{position:absolute;top:701px;width:167px;height:128px;border:4px solid #d3d3d3}
.photo-1{left:27px;background:linear-gradient(135deg,#5b6f80,#b7c0c9 60%,#4d5a3e)}
.photo-2{left:207px;background:linear-gradient(160deg,#cfd8df,#8b9aa6 60%,#e3e6e8)}

.news{left:445px;top:553px;width:160px}
.news-item{font-family:'Open Sans',sans-serif;font-size:10.5px;line-height:16.4px;color:#333}
.news-item a{display:block;text-align:right;color:var(--link-blue);text-decoration:none;padding-right:5px}
.news-item.first{margin-top:24px}
.news-item.second{margin-top:26px}

.contact-form{left:682px;top:553px;width:151px}
.contact-form label{display:block;font-family:'Open Sans',sans-serif;font-size:10.5px;color:#333;margin-top:14px;margin-bottom:5px}
.contact-form label.first{margin-top:18px}
.field{width:151px;height:22px;background:#fff;border:1px solid #cfcfcf}
.field.area{height:97px}

.site-footer{left:0;top:927px;width:873px;height:273px;background:linear-gradient(var(--footer-top),var(--footer-bottom))}
.foot-col{position:absolute;top:44px}
.foot-col h4{font-family:'Arimo',sans-serif;font-weight:700;font-size:10.5px;color:#fff;letter-spacing:.5px;margin-bottom:19px}
.foot-col a{display:block;font-size:10px;line-height:16.4px;color:#fff;text-decoration:none}
</style>
</head>
<body>

<header class="site-header abs">
  <div class="brand abs"><span class="brand-mark"></span><span class="brand-name">BRINMOOR GROUP</span></div>
  <nav class="main-nav">
    <a href="#" style="left:458px">COMPANY</a>
    <a href="#" class="active" style="left:555px">SERVICES</a>
    <a href="#" style="left:651px">CAREERS</a>
    <a href="#" style="left:743px">CONTACT US</a>
  </nav>
</header>
<div class="sub-band abs"></div>
<svg class="pointer abs" width="18" height="10" viewBox="0 0 18 10"><path d="M0 10 L9 1 L18 10Z" fill="#fafafa"/></svg>

<section class="hero abs">
  <div class="hero-image abs" role="img" aria-label="Wire shelving unit stacked with cardboard shipping boxes"></div>
  <h1 class="hero-title abs">Find Out Why Brinmoor is Right<br>For Your Business</h1>
  <svg class="cta abs" width="192" height="62" viewBox="0 0 192 62" role="img" aria-label="Get started">
    <defs><linearGradient id="ctaGrad" x1="0" y1="0" x2="0" y2="1"><stop offset="0" stop-color="#a5e04f"/><stop offset="1" stop-color="#5aab1c"/></linearGradient></defs>
    <path d="M0 9 H168 V0 L192 31 L168 62 V53 H0 Z" fill="url(#ctaGrad)" stroke="#4f9a18" stroke-width="1"/>
    <text x="16" y="39" font-family="Open Sans, sans-serif" font-size="20" font-weight="600" fill="#fff" letter-spacing="1.5">GET STARTED</text>
  </svg>
</section>

<section class="services abs">
  <div class="service" style="left:10px"><div class="service-icon" role="img" aria-label="Flat television and mobile phones" style="background:linear-gradient(#3b4a5c,#8b9bb0)"></div><div class="service-label">Remanufacture &amp;<br>Refurbishment Services</div></div>
  <div class="divider" style="left:194px"></div>
  <div class="service" style="left:189px"><div class="service-icon" role="img" aria-label="Blue globe" style="width:60px;border-radius:50%;background:radial-gradient(circle at 40% 35%,#9fd0ff,#1f5fc9)"></div><div class="service-label">Reverse Logistics<br>Management</div></div>
  <div class="divider" style="left:353px"></div>
  <div class="service" style="left:352px"><div class="service-icon" role="img" aria-label="Warranty papers with tools" style="width:70px;background:linear-gradient(#f1f1f1,#bdbdbd)"></div><div class="service-label">Warranty Repair &amp;<br>Field Service</div></div>
  <div class="divider" style="left:521px"></div>
  <div class="service" style="left:512px"><div class="service-icon" role="img" aria-label="Certified rubber stamp" style="width:70px;background:linear-gradient(#c93a3a,#f2dede)"></div><div class="service-label">Quality Control &amp;<br>Assurance</div></div>
  <div class="divider" style="left:686px"></div>
  <div class="service" style="left:695px"><div class="service-icon" role="img" aria-label="Warehouse racking with forklift" style="width:128px;background:linear-gradient(#2f6fc0,#d9d9d9)"></div><div class="service-label">Warehousing &amp;<br>Distribution</div></div>
</section>

<section class="about abs">
  <h2 class="section-title">WHAT WE DO</h2>
  <p>We are the return / refurbish / repair specialists behind the brand.</p>
  <p>For over 20 years, Brinmoor Group, Inc. has been serving the ever-growing consumer products industry. As a leading, large scale reverse logistics provider, we strive to deliver unsurpassed quality and support to manufacturers and their products.</p>
</section>
<div class="photo photo-1" role="img" aria-label="Technician soldering a circuit board under a magnifier"></div>
<div class="photo photo-2" role="img" aria-label="Open plan office with workstations"></div>

<section class="news abs">
  <h2 class="section-title">LATEST NEWS</h2>
  <div class="news-item first">Brinmoor, a large revers logistics services provider, is pleased to announce...<a href="#">Read More</a></div>
  <div class="news-item second">As more and more companies recognize their corporate responsibility...<a href="#">Read More</a></div>
</section>

<form class="contact-form abs">
  <h2 class="section-title">LEARN HOW BRINMOOR<br>CAN HELP</h2>
  <label class="first">Name</label><div class="field"></div>
  <label>Email</label><div class="field"></div>
  <label>Phone</label><div class="field"></div>
  <label>Comments</label><div class="field area"></div>
</form>

<footer class="site-footer abs">
  <div class="foot-col" style="left:223px"><h4>ABOUT US</h4><a href="#">CEO Letter</a><a href="#">Corporate Governance</a><a href="#">Environmental Health</a><a href="#">and Safety</a></div>
  <div class="foot-col" style="left:360px"><h4>SERVICES</h4><a href="#">Remanufacture and</a><a href="#">Refurbishment Services</a><a href="#">Factory Repair Services</a><a href="#">Reverse Logisics Management</a><a href="#">Quality Control and</a><a href="#">Assurance Services</a><a href="#">Warehousing and Distribution</a></div>
  <div class="foot-col" style="left:511px"><h4>CAREERS</h4><a href="#">Search Jobs</a></div>
  <div class="foot-col" style="left:627px"><h4>LOCATIONS</h4><a href="#">New Jersey</a><a href="#">Texas</a></div>
</footer>

</body>
</html>
```